Ledgrix Business Card

We need a business card design using the attached logo. The company is a financial services company that provides a dashboard (chart based information) for Executives of small businesses to use to better manage their information. The design must be progressive, make good utilization of the logo and project stability and financial security.

Industry/Entity Type

Financial

```html
<!DOCTYPE html>
<html lang="en">
<head>
<meta charset="utf-8">
<title>Ledgrix Business Card</title>
<link rel="stylesheet" href="https://fonts.googleapis.com/css2?family=Source+Sans+3:wght@400;600&display=swap">
<style>
  :root {
    --ink: #1a1a1a;
    --black: #000000;
    --white: #ffffff;
    --paper: #ffffff;
    --brand-red: #9b1c1f;
    --backdrop: #e6e3df;
    --text: #222222;
  }
  * { margin: 0; padding: 0; box-sizing: border-box; }
  html, body {
    width: 1191px;
    height: 1200px;
    overflow: hidden;
    background: var(--backdrop);
    font-family: "Source Sans 3", sans-serif;
  }
  .canvas { position: relative; width: 1191px; height: 1200px; }

  .card { position: absolute; width: 950px; height: 545px; }
  .card--front {
    left: 22px; top: 26px;
    background: var(--paper);
    box-shadow: 0 2px 6px rgba(0,0,0,0.25);
  }
  .card--back {
    left: 210px; top: 601px;
    background: var(--black);
    box-shadow: 0 2px 6px rgba(0,0,0,0.25);
  }

  .brand { position: absolute; left: 30px; top: 72px; display: flex; align-items: center; gap: 26px; }
  .brand__square { width: 118px; height: 118px; background: var(--brand-red); }
  .brand__name { font-size: 112px; font-weight: 600; color: var(--ink); line-height: 1; letter-spacing: -1px; }

  .edge-tab { position: absolute; }
  .edge-tab--left {
    left: 0; top: 299px; width: 17px; height: 213px;
    background: var(--black);
    border-radius: 0 10px 10px 0;
  }
  .edge-tab--right {
    right: 0; top: 364px; width: 17px; height: 83px;
    background: var(--brand-red);
    border-radius: 10px 0 0 10px;
  }

  .contact { position: absolute; left: 30px; top: 308px; list-style: none; }
  .contact__item {
    display: flex; align-items: center; gap: 10px;
    height: 35px;
    font-size: 23px; color: var(--text);
  }
  .contact__icon { width: 20px; height: 20px; fill: var(--brand-red); flex: none; }
  .contact__address { position: absolute; left: 30px; top: 460px; font-size: 23px; color: var(--text); }

  .person { position: absolute; right: 30px; top: 368px; text-align: right; }
  .person__name { font-size: 31px; font-weight: 600; color: var(--ink); line-height: 1.15; }
  .person__title { font-size: 24px; color: var(--brand-red); line-height: 1.2; }

  .back-brand {
    position: absolute; left: 0; right: 0; top: 160px;
    display: flex; justify-content: center; align-items: center; gap: 28px;
  }
  .back-brand__square { width: 130px; height: 130px; background: var(--white); }
  .back-brand__name { font-size: 124px; font-weight: 600; color: var(--white); line-height: 1; }
  .back-web {
    position: absolute; left: 0; right: 0; top: 460px;
    text-align: center; font-size: 28px; letter-spacing: 2px; color: var(--white);
  }
</style>
</head>
<body>
<main class="canvas">
  <section class="card card--front" aria-label="Card front">
    <div class="brand">
      <span class="brand__square"></span>
      <span class="brand__name">Ledgrix</span>
    </div>

    <span class="edge-tab edge-tab--left"></span>
    <ul class="contact">
      <li class="contact__item">
        <svg class="contact__icon" viewBox="0 0 20 20" aria-hidden="true"><path d="M5 2l3 4-2 2c1 2.5 3.5 5 6 6l2-2 4 3-2 3C9 18 2 11 2 4z"/></svg>
        012-345-6789
      </li>
      <li class="contact__item">
        <svg class="contact__icon" viewBox="0 0 20 20" aria-hidden="true"><path d="M6 1h8a1 1 0 0 1 1 1v16a1 1 0 0 1-1 1H6a1 1 0 0 1-1-1V2a1 1 0 0 1 1-1zm1 3v7h6V4zm1 9v2h1v-2zm2 0v2h1v-2zm2 0v2h1v-2z"/></svg>
        012-345-6789
      </li>
      <li class="contact__item">
        <svg class="contact__icon" viewBox="0 0 20 20" aria-hidden="true"><path d="M2 5h16v11H2zm1 1l7 6 7-6v-0.5H3z" fill-rule="evenodd"/><path d="M2 5l8 6 8-6v2l-8 6-8-6z"/></svg>
        info@ledgrix.com
      </li>
      <li class="contact__item">
        <svg class="contact__icon" viewBox="0 0 20 20" aria-hidden="true"><path d="M10 1a9 9 0 1 0 0 18 9 9 0 0 0 0-18zm0 2c1 1.3 1.7 3.2 1.9 5H8.1c.2-1.8.9-3.7 1.9-5zM3.1 8a7 7 0 0 1 3.7-4.2C6.3 5 6 6.5 6 8zm0 4H6c0 1.5.3 3 .8 4.2A7 7 0 0 1 3.1 12zm5 0h3.8c-.2 1.8-.9 3.7-1.9 5-1-1.3-1.7-3.2-1.9-5zm0-2h3.8v0H8.1zm5.9 2h2.9a7 7 0 0 1-3.7 4.2c.5-1.2.8-2.7.8-4.2zm0-4c0-1.5-.3-3-.8-4.2A7 7 0 0 1 16.9 8z"/></svg>
        www.ledgrix.com
      </li>
    </ul>
    <p class="contact__address">Street Name, City Name, Zip Code-00000</p>

    <div class="person">
      <p class="person__name">Your Name</p>
      <p class="person__title">Title</p>
    </div>
    <span class="edge-tab edge-tab--right"></span>
  </section>

  <section class="card card--back" aria-label="Card back">
    <div class="back-brand">
      <span class="back-brand__square"></span>
      <span class="back-brand__name">Ledgrix</span>
    </div>
    <p class="back-web">www.ledgrix.com</p>
  </section>
</main>
</body>
</html>
```